Hospital Digital Whiteboard UI/UX Redesign

We are looking to update the look and feel of our Digital Whiteboards.
There are 4 separate layouts: Patient TV, Patient Room Whiteboard, Digital Door Sign, and Unit Care Board.
We want to have a unified, modern look across the portfolio.

```html
<!DOCTYPE html>
<html lang="en">
<head>
<meta charset="utf-8">
<title>Patient Room Whiteboard</title>
<link href="https://fonts.googleapis.com/css2?family=Montserrat:wght@400;500;600&display=swap" rel="stylesheet">
<style>
:root{
  --navy:#0a23a8;
  --blue-top:#1d63d6;
  --blue-deep:#0b1fa3;
  --teal:#4decd8;
  --ink:#0d2aa8;
  --text:#3a3f4a;
  --muted:#8a8f99;
  --line:#e3e7ec;
  --card:#ffffff;
  --bg:#ffffff;
}
*{box-sizing:border-box;margin:0;padding:0}
html,body{width:1200px;height:675px;overflow:hidden;background:var(--bg);font-family:"Montserrat",sans-serif;color:var(--text)}
.board{position:relative;width:1200px;height:675px}
.abs{position:absolute}

.topbar{left:0;top:0;width:1200px;height:77px;border-radius:0 0 25px 25px;background:linear-gradient(180deg,var(--blue-top),var(--blue-deep));color:#fff}
.avatar{left:19px;top:15px;width:34px;height:34px;border-radius:50%;background:var(--teal)}
.patient{left:68px;top:20px;font-size:20px;font-weight:500}
.clock{left:0;width:1200px;top:11px;text-align:center;font-size:19px;font-weight:500;line-height:28px}
.room{right:20px;top:22px;font-size:20px;font-weight:500}

.panel{background:var(--card);box-shadow:0 1px 6px rgba(0,0,0,.08)}
.panel-head{height:36px;background:var(--teal);color:#fff;font-size:17px;font-weight:500;text-align:center;line-height:37px;letter-spacing:.3px}

.goals{left:19px;top:82px;width:359px;height:324px}
.goal-label{color:var(--ink);font-size:18px;font-weight:600;line-height:28px}
.goal-value{color:var(--teal);font-size:16px;font-weight:500}
.divider-v{left:151px;top:50px;width:1px;height:260px;background:var(--line)}
.divider-h{left:11px;top:96px;width:330px;height:1px;background:var(--line)}
.checklist{left:165px;top:109px;width:190px;list-style:none;font-size:16.5px;line-height:24px}
.checklist li{position:relative;padding-left:18px;margin-bottom:8px}
.checklist svg{position:absolute;left:0;top:8px}

.ambulation{left:19px;top:414px;width:359px;height:247px}
.track{left:38px;top:490px;width:1px;height:100px;background:#c8ccd3}
.step-dot{width:19px;height:19px;border-radius:50%;border:1.5px solid #c8ccd3;background:#fff}
.step-dot.active{border-color:var(--ink);background:radial-gradient(circle,var(--ink) 0 5.5px,#fff 6px)}
.step{left:72px;width:304px}
.step-title{font-size:15.5px;font-weight:500;color:var(--muted);line-height:22px;letter-spacing:-.2px}
.step-title.single{white-space:nowrap}
.step.active .step-title{color:var(--ink)}
.step-date{font-size:12.5px;color:#a4a8b0;margin-top:1px;line-height:16px}
.step.active .step-date{color:var(--text)}

.care{left:394px;top:82px;width:412px;height:398px}
.member{left:8px;width:396px;height:62px;border:1px solid var(--line);border-radius:4px;background:#fff}
.photo{position:absolute;left:7px;top:6px;width:55px;height:50px;border-radius:3px;background:linear-gradient(160deg,#9db3c9,#5d6f86)}
.role{position:absolute;left:98px;top:12px;font-size:13px}
.name{position:absolute;left:98px;top:34px;font-size:13px}
.phone{position:absolute;left:226px;top:34px;font-size:13px;display:flex;align-items:center;gap:8px}

.brand{left:394px;top:502px;width:414px;height:69px;border-radius:14px;display:flex;align-items:center;justify-content:center;gap:8px;color:#3dbb4b;font-size:22px;font-weight:500}
.brand-dot{width:14px;height:14px;border-radius:50%;background:#3dbb4b}

.btn{top:583px;width:198px;height:59px;border-radius:10px;background:var(--navy);color:#fff;display:flex;align-items:center;justify-content:center;gap:16px;font-size:18px;font-weight:500}
.btn-icon{width:34px;height:34px;border-radius:50%;background:var(--teal);display:flex;align-items:center;justify-content:center}

.discharge{left:822px;top:82px;width:359px;height:137px}
.discharge-body{height:101px;background:linear-gradient(180deg,var(--blue-top),var(--blue-deep));color:#fff;font-size:36px;font-weight:500;text-align:center;line-height:101px}

.dose{left:822px;top:227px;width:359px;height:179px}
.dose-card{left:5px;width:348px;height:62px;border:1px solid var(--line);border-radius:4px;background:#fff}
.pills{position:absolute;left:20px;top:8px;width:140px;height:46px;border-radius:23px}
.dose-card .sep{position:absolute;left:173px;top:8px;width:1px;height:46px;background:var(--line)}
.med{position:absolute;left:216px;top:12px;font-size:13px}
.med-time{position:absolute;left:216px;top:31px;font-size:16px;font-weight:600;color:var(--ink)}

.family{left:822px;top:417px;width:359px;height:141px}
.contact{left:5px;width:348px;height:43px;border:1px solid var(--line);border-radius:4px;background:#fff;display:flex;align-items:center;justify-content:space-between;padding:0 18px;font-size:13px}
.contact strong{color:var(--ink);font-size:16px;font-weight:600}
</style>
</head>
<body>
<div class="board">

  <header class="abs topbar">
    <div class="abs avatar">
      <svg width="34" height="34" viewBox="0 0 34 34"><circle cx="17" cy="13" r="5" fill="#fff"/><path d="M8 26a9 7 0 0 1 18 0z" fill="#fff"/></svg>
    </div>
    <div class="abs patient">Whitmore, Paul</div>
    <div class="abs clock">10:23 am<br>Thyrsday, October 25th 2018</div>
    <div class="abs room">Room 5131</div>
  </header>

  <section class="abs panel goals">
    <div class="panel-head">GOALS</div>
    <div class="abs goal-label" style="left:25px;top:59px">Today's Goal</div>
    <div class="abs goal-value" style="left:167px;top:63px">Walk 25 Feet</div>
    <div class="abs divider-v"></div>
    <div class="abs divider-h"></div>
    <div class="abs goal-label" style="left:25px;top:106px">Discharge<br>Goals</div>
    <ul class="abs checklist">
      <li><svg width="10" height="8" viewBox="0 0 10 8"><path d="M1 4l3 3 5-6" fill="none" stroke="#4decd8" stroke-width="1.8"/></svg>Complete comprehension tests</li>
      <li><svg width="10" height="8" viewBox="0 0 10 8"><path d="M1 4l3 3 5-6" fill="none" stroke="#4decd8" stroke-width="1.8"/></svg>Review medications</li>
      <li><svg width="10" height="8" viewBox="0 0 10 8"><path d="M1 4l3 3 5-6" fill="none" stroke="#4decd8" stroke-width="1.8"/></svg>Explain test results</li>
      <li><svg width="10" height="8" viewBox="0 0 10 8"><path d="M1 4l3 3 5-6" fill="none" stroke="#4decd8" stroke-width="1.8"/></svg>Schedule follow-up appointment</li>
    </ul>
  </section>

  <section class="abs panel ambulation">
    <div class="panel-head">AMBULATION STATUS</div>
  </section>
  <div class="abs track"></div>
  <div class="abs step-dot active" style="left:29px;top:471px"></div>
  <div class="abs step-dot" style="left:29px;top:527px"></div>
  <div class="abs step-dot" style="left:29px;top:581px"></div>
  <div class="abs step active" style="top:469px"><div class="step-title single">Moving with support inside room</div><div class="step-date">10/21/18</div></div>
  <div class="abs step" style="top:525px"><div class="step-title single">Walking around in hall w/ crutches</div><div class="step-date">10/21/18</div></div>
  <div class="abs step" style="top:580px"><div class="step-title">Can walk around hall with no help from staff</div><div class="step-date">10/21/18</div></div>

  <section class="abs panel care">
    <div class="panel-head">CARE TEAM</div>
    <div class="abs member" style="top:45px"><div class="photo" role="img" aria-label="Portrait of the nurse manager"></div><div class="role">Nurse Manager</div><div class="name">Laura Kemp, R.N.</div><div class="phone"><svg width="11" height="11" viewBox="0 0 24 24"><path d="M6.6 10.8a15 15 0 0 0 6.6 6.6l2.2-2.2c.3-.3.7-.4 1-.2 1.1.4 2.3.6 3.6.6.6 0 1 .4 1 1V20c0 .6-.4 1-1 1A17 17 0 0 1 3 4c0-.6.4-1 1-1h3.5c.6 0 1 .4 1 1 0 1.3.2 2.5.6 3.6.1.3 0 .7-.2 1z" fill="#0a23a8"/></svg>555-010-2114</div></div>
    <div class="abs member" style="top:115px"><div class="photo" role="img" aria-label="Portrait of the charge nurse"></div><div class="role">Charge Nurse</div><div class="name">Dana Morrow</div><div class="phone"><svg width="11" height="11" viewBox="0 0 24 24"><path d="M6.6 10.8a15 15 0 0 0 6.6 6.6l2.2-2.2c.3-.3.7-.4 1-.2 1.1.4 2.3.6 3.6.6.6 0 1 .4 1 1V20c0 .6-.4 1-1 1A17 17 0 0 1 3 4c0-.6.4-1 1-1h3.5c.6 0 1 .4 1 1 0 1.3.2 2.5.6 3.6.1.3 0 .7-.2 1z" fill="#0a23a8"/></svg>555-010-2115</div></div>
    <div class="abs member" style="top:186px"><div class="photo" role="img" aria-label="Portrait of the duty nurse"></div><div class="role">Duty Nurse</div><div class="name">Tessa Boyd</div><div class="phone"><svg width="11" height="11" viewBox="0 0 24 24"><path d="M6.6 10.8a15 15 0 0 0 6.6 6.6l2.2-2.2c.3-.3.7-.4 1-.2 1.1.4 2.3.6 3.6.6.6 0 1 .4 1 1V20c0 .6-.4 1-1 1A17 17 0 0 1 3 4c0-.6.4-1 1-1h3.5c.6 0 1 .4 1 1 0 1.3.2 2.5.6 3.6.1.3 0 .7-.2 1z" fill="#0a23a8"/></svg>555-010-2116</div></div>
    <div class="abs member" style="top:256px"><div class="photo" role="img" aria-label="Portrait of the patient care tech"></div><div class="role">Patient Care Tech</div><div class="name">Ravi Mehta</div><div class="phone"><svg width="11" height="11" viewBox="0 0 24 24"><path d="M6.6 10.8a15 15 0 0 0 6.6 6.6l2.2-2.2c.3-.3.7-.4 1-.2 1.1.4 2.3.6 3.6.6.6 0 1 .4 1 1V20c0 .6-.4 1-1 1A17 17 0 0 1 3 4c0-.6.4-1 1-1h3.5c.6 0 1 .4 1 1 0 1.3.2 2.5.6 3.6.1.3 0 .7-.2 1z" fill="#0a23a8"/></svg>555-010-2117</div></div>
    <div class="abs member" style="top:326px"><div class="photo" role="img" aria-label="Portrait of the social worker"></div><div class="role">Social Worker</div><div class="name">Owen Bradley</div><div class="phone"><svg width="11" height="11" viewBox="0 0 24 24"><path d="M6.6 10.8a15 15 0 0 0 6.6 6.6l2.2-2.2c.3-.3.7-.4 1-.2 1.1.4 2.3.6 3.6.6.6 0 1 .4 1 1V20c0 .6-.4 1-1 1A17 17 0 0 1 3 4c0-.6.4-1 1-1h3.5c.6 0 1 .4 1 1 0 1.3.2 2.5.6 3.6.1.3 0 .7-.2 1z" fill="#0a23a8"/></svg>555-010-2118</div></div>
  </section>

  <div class="abs panel brand"><span class="brand-dot"></span>Lumen Health</div>

  <div class="abs btn" style="left:394px">
    <span class="btn-icon"><svg width="14" height="16" viewBox="0 0 14 16"><rect x="1" y="7" width="12" height="9" rx="1.5" fill="#fff"/><path d="M4 7V5a3 3 0 0 1 6 0v2" fill="none" stroke="#fff" stroke-width="2"/></svg></span>Admin
  </div>
  <div class="abs btn" style="left:609px">
    <span class="btn-icon"><svg width="14" height="18" viewBox="0 0 14 18"><path d="M7 0a7 7 0 0 0-7 7c0 5 7 11 7 11s7-6 7-11a7 7 0 0 0-7-7z" fill="#fff"/><circle cx="7" cy="7" r="2.5" fill="#4decd8"/></svg></span>Floor Map
  </div>

  <section class="abs discharge">
    <div class="panel-head">ANTICIPATED DAY OF DISCHARGE</div>
    <div class="discharge-body">12 May 2018</div>
  </section>

  <section class="abs panel dose">
    <div class="panel-head">NEXT DOSE</div>
    <div class="abs dose-card" style="top:43px"><div class="pills" role="img" aria-label="White round tablets" style="background:linear-gradient(90deg,#fff,#e9ecef,#fff)"></div><div class="sep"></div><div class="med">Oxycodone 5mg</div><div class="med-time">11:00 am</div></div>
    <div class="abs dose-card" style="top:110px"><div class="pills" role="img" aria-label="Orange oval tablets" style="background:linear-gradient(90deg,#f3c98f,#e7a35c,#f3c98f)"></div><div class="sep"></div><div class="med">Odansetron 8mg</div><div class="med-time">11:30 pm</div></div>
  </section>

  <section class="abs panel family">
    <div class="panel-head">FAMILY CONTACT</div>
    <div class="abs contact" style="top:43px">Mark Whitmore<strong>555-020-7390</strong></div>
    <div class="abs contact" style="top:92px">Ellen Whitmore<strong>555-020-7390</strong></div>
  </section>

</div>
</body>
</html>
```